Veltrion Knowledge Enhancement Company Website

Veltrion is knowledge enhancement Highend and Deep Technology Company who has training programs in Applied Quantum, Applied Artificial Intelligence and Data Science. All the technologies are very advanced and future technologies and the website should reflect the technology advancement. Looking for a sophisticated web design which will reflect our focus on deep and future technologies. Logo file is uploaded

Target Market(s)

Big Corporates and Premium Colleges

Industry/Entity Type

Technology, Deep Technology, Future Technology

Coding

Coded - Design and coding required

Number of Pages Required

5+ page

Requirements
Must have
• A Very Contemporary clean look and should reflect Future Technologies
Nice to have
• Should be very Classy
Should not have
• Traditional Fonts and Colors

```html
<!DOCTYPE html>
<html lang="en">
<head>
<meta charset="utf-8">
<title>Veltrion — Knowledge Enhancement</title>
<link href="https://fonts.googleapis.com/css2?family=Marcellus&family=Poppins:wght@300;400;500;600&display=swap" rel="stylesheet">
<style>
:root{
  --blue:#1ea0e0;
  --blue-soft:#8fd0f2;
  --ink:#121212;
  --muted:#6f6f6f;
  --tint:#f4f9fd;
  --navy:#0a1033;
  --white:#ffffff;
}
*{margin:0;padding:0;box-sizing:border-box}
html,body{width:1200px;height:3728px;overflow:hidden}
body{position:relative;background:var(--white);font-family:'Poppins',sans-serif;color:var(--ink)}
.abs{position:absolute}
.serif{font-family:'Marcellus',serif;font-weight:400}
.label{position:absolute;left:164px;color:var(--blue);font-size:17px;font-weight:500;letter-spacing:1px}
.h2{position:absolute;left:162px;font-family:'Marcellus',serif;font-size:36px;line-height:45px;color:var(--ink)}
.copy{position:absolute;font-size:13.5px;line-height:23px;color:#555;font-weight:400}
.btn{position:absolute;height:38px;background:var(--blue);color:var(--white);font-size:15px;display:flex;align-items:center;justify-content:center}
.btn .dots{position:absolute;left:-10px;top:-8px;width:34px;height:30px}
.btn .dots i{position:absolute;width:5px;height:5px;background:var(--blue)}
.nav{position:absolute;top:44px;font-size:15px;color:#222}
.nav.active{color:var(--blue)}
.logo{position:absolute;display:flex;align-items:center;gap:10px;font-family:'Poppins',sans-serif;font-weight:500;font-size:22px;color:var(--blue)}
.logo .mark{width:34px;height:34px;background:var(--blue);border-radius:4px}
.diamond{position:absolute;width:26px;height:26px;background:#9fd6f3;transform:rotate(45deg)}
.art{position:absolute;border-radius:24px}
.prog-icon{position:absolute;top:1455px;width:56px;height:56px}
.prog-title{position:absolute;top:1527px;font-size:19px;font-weight:500}
.prog-copy{position:absolute;top:1560px;width:222px;font-size:14px;line-height:24.5px;color:#888;text-align:justify}
.check{position:absolute;left:162px;display:flex;align-items:center;gap:9px;font-size:14px;color:#222}
.check svg{width:16px;height:16px}
.card{position:absolute;top:2895px;width:278px;height:434px;background:var(--white);border-radius:0 0 26px 26px;box-shadow:0 10px 24px rgba(20,60,110,.08);overflow:hidden}
.card .pic{height:203px;border-radius:22px 0 0 0}
.card .meta{position:absolute;left:23px;top:232px;font-size:12px;color:#999}
.card h3{position:absolute;left:23px;top:260px;width:240px;font-size:17px;line-height:23px;font-weight:500}
.card p{position:absolute;left:23px;top:314px;width:240px;font-size:12px;line-height:19px;color:#888}
.card .more{position:absolute;left:23px;top:382px;font-size:13px;color:var(--blue);display:flex;align-items:center;gap:8px}
.footer{position:absolute;left:0;top:3420px;width:1200px;height:308px;background:var(--navy);color:var(--white)}
.footer .nav{color:var(--white);top:64px}
.f-item{position:absolute;top:170px;display:flex;gap:14px;font-size:14px;line-height:22px}
.f-item svg{width:34px;height:34px;flex:none}
.social{position:absolute;top:262px;width:23px;height:23px;border-radius:50%;background:var(--blue)}
</style>
</head>
<body>

<!-- HERO -->
<section class="abs" style="left:0;top:0;width:1200px;height:593px;background:linear-gradient(180deg,#ffffff 0%,#f3f9fd 100%)">
  <div class="abs" style="left:0;top:250px;width:110px;height:230px;background:linear-gradient(90deg,#dff0fb,rgba(223,240,251,0))"></div>
  <div class="logo" style="left:160px;top:34px"><span class="mark"></span>Veltrion</div>
  <span class="nav active" style="left:541px">Home</span>
  <span class="nav" style="left:634px">About Us</span>
  <span class="nav" style="left:753px">Program</span>
  <span class="nav" style="left:868px">News</span>
  <span class="nav" style="left:957px">Contact Us</span>

  <div class="abs" style="left:164px;top:258px;font-size:19px;color:var(--blue)">Applying Data Science</div>
  <h1 class="abs serif" style="left:162px;top:292px;font-size:38px;line-height:47px">And Techniques with<br>Systems</h1>
  <div class="btn" style="left:169px;top:415px;width:150px;height:42px">
    <span class="dots"><i style="left:0;top:10px"></i><i style="left:8px;top:2px"></i><i style="left:14px;top:12px"></i><i style="left:4px;top:20px"></i></span>Contact Us</div>
  <div class="art" role="img" aria-label="Isometric illustration of server racks, a laptop with data charts and bar graphs" style="left:565px;top:152px;width:535px;height:376px;background:linear-gradient(135deg,#cfe6fb 0%,#9ccaf3 55%,#e3eefb 100%)"></div>
</section>

<!-- ABOUT -->
<section class="abs" style="left:0;top:593px;width:1200px;height:666px">
  <div class="diamond" style="left:55px;top:36px"></div>
  <div class="diamond" style="left:-12px;top:100px"></div>
  <div class="diamond" style="left:30px;top:360px"></div>
  <div class="diamond" style="left:1113px;top:568px"></div>
  <div class="art" role="img" aria-label="Isometric illustration of people working with servers, a cloud upload and a laptop" style="left:94px;top:102px;width:442px;height:477px;background:linear-gradient(135deg,#dcebfb 0%,#8fbde9 60%,#e9f1fb 100%)"></div>
  <div class="label" style="left:609px;top:156px">ABOUT US</div>
  <div class="h2" style="left:609px;top:182px">Veltrion Technology<br>Training</div>
  <p class="copy" style="left:609px;top:289px;width:433px;text-align:justify">Quantum computing could be the most significant technological revolution since the internet's inception. According to experts, the market for quantum technologies will quadruple by 2029. There has never been a better time to get involved in a thriving industry like quantum computing.</p>
  <p class="copy" style="left:609px;top:413px;width:433px;text-align:justify">Quantum technology will necessitate far more than project managers and theoretical physicists.</p>
  <div class="btn" style="left:620px;top:493px;width:137px">
    <span class="dots"><i style="left:0;top:10px"></i><i style="left:8px;top:2px"></i><i style="left:14px;top:12px"></i><i style="left:4px;top:20px"></i></span>Read More</div>
</section>

<!-- PROGRAM -->
<section class="abs" style="left:0;top:1259px;width:1200px;height:471px;background:var(--tint)"></section>
<div class="label" style="top:1352px">PROGRAM</div>
<div class="h2" style="top:1375px">Our Training Program</div>
<p class="copy" style="left:614px;top:1347px;width:428px">Lorem ipsum dolor sit amet, consectetur adipiscing elit. itempor lacus, sit amet fringilla neque. Aliquam vel porta erat. ano neque Suspendisse ut vehicula ex.</p>

<svg class="prog-icon" style="left:162px" viewBox="0 0 56 56" fill="none" stroke="#111" stroke-width="2">
  <rect x="8" y="8" width="40" height="40"/><rect x="14" y="14" width="28" height="28" stroke="var(--blue)"/>
  <circle cx="28" cy="28" r="4" stroke="var(--blue)"/><ellipse cx="28" cy="28" rx="11" ry="4" stroke="var(--blue)"/>
  <path d="M14 2v6M22 2v6M30 2v6M38 2v6M14 48v6M22 48v6M30 48v6M38 48v6M2 16h6M2 24h6M2 32h6M2 40h6M48 16h6M48 24h6M48 32h6M48 40h6"/>
</svg>
<svg class="prog-icon" style="left:461px" viewBox="0 0 56 56" fill="none" stroke="#111" stroke-width="2">
  <circle cx="28" cy="28" r="10" stroke="var(--blue)"/><circle cx="28" cy="28" r="16"/>
  <path d="M28 4v8M28 44v8M4 28h8M44 28h8M11 11l6 6M39 39l6 6M45 11l-6 6M17 39l-6 6"/>
  <circle cx="28" cy="4" r="2"/><circle cx="28" cy="52" r="2"/><circle cx="4" cy="28" r="2"/><circle cx="52" cy="28" r="2"/>
</svg>
<svg class="prog-icon" style="left:814px" viewBox="0 0 56 56" fill="none" stroke="#111" stroke-width="2">
  <ellipse cx="28" cy="14" rx="10" ry="4" stroke="var(--blue)"/><path d="M18 14v24c0 2 4 4 10 4s10-2 10-4V14M18 26c0 2 4 4 10 4s10-2 10-4" stroke="var(--blue)"/>
  <path d="M4 10h10M4 22h10M4 34h10M4 46h10M42 10h10M42 22h10M42 34h10M42 46h10"/>
  <circle cx="4" cy="10" r="2"/><circle cx="52" cy="46" r="2"/><circle cx="4" cy="46" r="2"/><circle cx="52" cy="10" r="2"/>
</svg>

<div class="prog-title" style="left:162px">Applied Quantum</div>
<div class="prog-title" style="left:463px;top:1530px">Applied Artificial Intelligence</div>
<div class="prog-title" style="left:815px;top:1530px">Data Science</div>
<p class="prog-copy" style="left:163px">Lorem ipsum dolor sit amet, elit consectetuer elit adipiscing ie no Lorem ipsum dolor sit amet consectetuer adipiscing .</p>
<p class="prog-copy" style="left:463px;width:260px">Lorem ipsum dolor sit fringilla amet, consectetur adipiscing ipsum neque elit. Pellentesque in tempor it lacus, amet sit amet fringilla neque.</p>
<p class="prog-copy" style="left:815px">Lorem ipsum dolor sit amet, elit consectetuer elit adipiscing ie no Lorem ipsum dolor sit amet consectetuer adipiscing .</p>

<!-- FEATURE -->
<div class="diamond" style="left:75px;top:2205px"></div>
<div class="diamond" style="left:12px;top:2270px"></div>
<div class="label" style="top:1837px">LOREM IPSUM</div>
<div class="h2" style="top:1862px">Lorem ipsum dolor sit amet,<br>consectetur</div>
<p class="copy" style="left:164px;top:1968px;width:435px;text-align:justify">Lorem ipsum dolor amet nosit amet, consectetur adipiscing elit. Pellentesque in tempor lacus, sit amet fringilla neque. Aliquam vel porta erat. Suspendisse ut vehicula ex.</p>
<div class="check" style="top:2054px"><svg viewBox="0 0 16 16"><circle cx="8" cy="8" r="8" fill="#1ea0e0"/><path d="M4.5 8.2l2.3 2.3 4.7-4.8" stroke="#fff" stroke-width="1.8" fill="none"/></svg>Lorem ipsum dolor sit , consectetur adipiscing elit.</div>
<div class="check" style="top:2087px"><svg viewBox="0 0 16 16"><circle cx="8" cy="8" r="8" fill="#1ea0e0"/><path d="M4.5 8.2l2.3 2.3 4.7-4.8" stroke="#fff" stroke-width="1.8" fill="none"/></svg>Sed nec suscipit sapien, eu no tempor non &nbsp;lectus.</div>
<div class="check" style="top:2120px"><svg viewBox="0 0 16 16"><circle cx="8" cy="8" r="8" fill="#1ea0e0"/><path d="M4.5 8.2l2.3 2.3 4.7-4.8" stroke="#fff" stroke-width="1.8" fill="none"/></svg>Duis tincidunt elementum ligula, non lacinia mi vel.</div>
<div class="btn" style="left:169px;top:2180px;width:138px">
  <span class="dots"><i style="left:0;top:10px"></i><i style="left:8px;top:2px"></i><i style="left:14px;top:12px"></i><i style="left:4px;top:20px"></i></span>Read More</div>
<div class="art" role="img" aria-label="Isometric illustration of a person with a laptop showing a dashboard, charts and a pie chart" style="left:644px;top:1802px;width:456px;height:442px;background:linear-gradient(135deg,#e5f0fb 0%,#9ec5ec 55%,#eef4fb 100%)"></div>

<!-- CTA -->
<section class="abs" style="left:0;top:2333px;width:1200px;height:355px;background:linear-gradient(120deg,#2aa7e6 0%,#1e9fdf 60%,#1a95d6 100%);color:var(--white);text-align:center">
  <h2 class="serif" style="position:absolute;left:0;top:95px;width:1200px;font-size:34px">Get Ready to StartYour Project With Us</h2>
  <p style="position:absolute;left:258px;top:150px;width:684px;font-size:13.5px;line-height:21px">Lorem ipsum dolor sit amet, consectetur adipiscing elit. Pellentesque in tempor lacus, sit amet fringilla neque. Aliquam vel porta erat. Suspendisse ut vehicula ex. Duis tincidunt elementum ligula.</p>
  <div class="btn" style="left:537px;top:226px;width:138px;height:37px;background:var(--white);color:var(--blue)">
    <span class="dots"><i style="left:0;top:10px;background:#fff"></i><i style="left:8px;top:2px;background:#fff"></i><i style="left:14px;top:12px;background:#fff"></i><i style="left:4px;top:20px;background:#fff"></i></span>Contact Us</div>
</section>

<!-- NEWS -->
<div class="diamond" style="left:1090px;top:3300px"></div>
<div class="diamond" style="left:1153px;top:3365px"></div>
<div class="label" style="top:2782px">NEWS</div>
<div class="h2" style="top:2807px">Recent Blogs And News</div>
<p class="copy" style="left:614px;top:2782px;width:428px">Lorem ipsum dolor sit amet, consectetur adipiscing elit. itempor lacus, sit amet fringilla neque. Aliquam vel porta erat. ano neque Suspendisse ut vehicula ex.</p>

<article class="card" style="left:162px">
  <div class="pic" role="img" aria-label="Photo of a glowing AI circuit board" style="background:linear-gradient(135deg,#5a2a7a 0%,#2a3f8f 55%,#14245e 100%)"></div>
  <div class="meta">13/01/2022— Marta K.</div>
  <h3>Lorem Ipsum Dolor Sit Amet Con Se Ctetuer Adipis.</h3>
  <p>sed diam nonummy it mnibh euismod tinci dunt ut it no laoreet dolore magna aliquam erat volutpat Ut wisi ad.</p>
  <div class="more">Read More <svg width="16" height="8" viewBox="0 0 16 8"><path d="M0 4h14M11 1l3 3-3 3" stroke="#1ea0e0" stroke-width="1.6" fill="none"/></svg></div>
</article>
<article class="card" style="left:462px">
  <div class="pic" role="img" aria-label="Photo of a neon-lit data center corridor" style="background:linear-gradient(180deg,#0b5f6e 0%,#123a55 50%,#c25a3a 100%)"></div>
  <div class="meta">13/01/2022— Marta K.</div>
  <h3>Lorem Ipsum Dolor Sit Amet Con Se Ctetuer Adipis.</h3>
  <p>sed diam nonummy it mnibh euismod tinci dunt ut it no laoreet dolore magna aliquam erat volutpat Ut wisi ad.</p>
  <div class="more">Read More <svg width="16" height="8" viewBox="0 0 16 8"><path d="M0 4h14M11 1l3 3-3 3" stroke="#1ea0e0" stroke-width="1.6" fill="none"/></svg></div>
</article>
<article class="card" style="left:761px">
  <div class="pic" role="img" aria-label="Photo of a glowing digital globe" style="background:radial-gradient(circle at 30% 40%,#2d7fd6 0%,#0e2a78 45%,#070f3a 100%)"></div>
  <div class="meta">13/01/2022— Marta K.</div>
  <h3>Lorem Ipsum Dolor Sit Amet Con Se Ctetuer Adipis.</h3>
  <p>sed diam nonummy it mnibh euismod tinci dunt ut it no laoreet dolore magna aliquam erat volutpat Ut wisi ad.</p>
  <div class="more">Read More <svg width="16" height="8" viewBox="0 0 16 8"><path d="M0 4h14M11 1l3 3-3 3" stroke="#1ea0e0" stroke-width="1.6" fill="none"/></svg></div>
</article>

<!-- FOOTER -->
<footer class="footer">
  <div class="logo" style="left:162px;top:52px"><span class="mark"></span>Veltrion</div>
  <span class="nav" style="left:541px">Home</span>
  <span class="nav" style="left:634px">About Us</span>
  <span class="nav" style="left:753px">Program</span>
  <span class="nav" style="left:868px">News</span>
  <span class="nav" style="left:957px">Contact Us</span>
  <div class="abs" style="left:162px;top:136px;width:877px;height:1px;background:rgba(255,255,255,.12)"></div>

  <div class="f-item" style="left:162px">
    <svg viewBox="0 0 34 34" fill="none" stroke="#1ea0e0" stroke-width="1.6"><path d="M17 28s-8-9-8-15a8 8 0 0116 0c0 6-8 15-8 15z"/><circle cx="17" cy="13" r="3"/><path d="M6 30h22"/></svg>
    <div>123, building name, street City,<br>State XY 123456</div></div>
  <div class="f-item" style="left:517px">
    <svg viewBox="0 0 34 34" fill="none" stroke="#1ea0e0" stroke-width="1.6"><path d="M8 5l5 1 2 6-3 2c1 3 4 6 7 7l2-3 6 2 1 5c-1 2-3 3-5 3C13 28 6 21 6 9c0-2 1-3 2-4z"/><path d="M20 6a8 8 0 018 8M20 10a4 4 0 014 4"/></svg>
    <div>Phone<br>+ 1 123 456 7890</div></div>
  <div class="f-item" style="left:805px">
    <svg viewBox="0 0 34 34" fill="none" stroke="#1ea0e0" stroke-width="1.6"><rect x="4" y="10" width="26" height="18"/><path d="M4 10l13 10 13-10M9 10V4h16v6M12 8h10"/></svg>
    <div>E-Mail<br>info@veltrion.com</div></div>

  <div class="abs" style="left:162px;top:262px;font-size:13.5px">© 2023 Veltrion. All Rights Reserved.</div>
  <span class="social" style="left:908px"></span>
  <span class="social" style="left:943px"></span>
  <span class="social" style="left:978px"></span>
  <span class="social" style="left:1014px"></span>
</footer>

</body>
</html>
```